Business Card Design

We are a new residential construction company.our team is made up of young highly skilled tradesman of the next generation of carpenters coming through with new skills and ideas.we chose the name meridian as it means strikingly different from the rest as this is what we plan to be and we would like to portray this in our business card.we like Bold lettering as we want to make a statement, also the use of colour would be great as we want to stand out from the usual plain construction cards and logos.
I have attached a logo sketch I did as a rough idea if you can tidy it up or improve on it would be good.
I have also attached the LBP logo please include this on the card small but still legible.
open to any colourschemes ideas.
thanks
(note)please delete the LBP#308617 off from the card details please.
Updates
Industry/Entity Type
Construction
Contact Information for Business Card
MERIDIAN CONSTRUCTION LIMITED
Director:Kai Pereira
Mobile :0217364801
Email:Meridian.Construction@examplemail.test
Address:48 Halvorsen place,Ashgrove park 2071,Auckland
LBP#BP308617
Look and feel
Each slider illustrates characteristics of the customer's brand and the style your logo design should communicate.

```html
<!DOCTYPE html>
<html lang="en">
<head>
<meta charset="utf-8">
<title>Meridian Construction Limited – Business Card</title>
<link href="https://fonts.googleapis.com/css2?family=Arimo:ital,wght@0,400;0,700;1,400;1,700&display=swap" rel="stylesheet">
<style>
  :root {
    --card-bg: #000000;
    --text-main: #ffffff;
    --badge-bg: #ffffff;
  }
  * { margin: 0; padding: 0; box-sizing: border-box; }
  html, body {
    width: 1200px;
    height: 741px;
    overflow: hidden;
    background: var(--card-bg);
  }
  .card {
    position: relative;
    width: 1200px;
    height: 741px;
    background: var(--card-bg);
    color: var(--text-main);
    font-family: "Arimo", Arial, sans-serif;
  }
  .brand {
    position: absolute;
    left: 71px;
    top: 120px;
    display: flex;
    align-items: center;
    gap: 14px;
  }
  .brand-square {
    width: 34px;
    height: 34px;
    background: var(--text-main);
  }
  .brand-name {
    font-weight: 700;
    font-size: 34px;
    line-height: 1.1;
    letter-spacing: 1px;
    color: var(--text-main);
  }
  .person {
    position: absolute;
    right: 72px;
    top: 80px;
    text-align: right;
  }
  .person-name {
    font-weight: 700;
    font-size: 52px;
    line-height: 1;
  }
  .person-role {
    font-style: italic;
    font-size: 39px;
    line-height: 1;
    margin-top: 14px;
  }
  .company-title {
    position: absolute;
    left: 0;
    right: 0;
    top: 345px;
    text-align: center;
    font-weight: 700;
    font-size: 47px;
    line-height: 1;
    letter-spacing: 0.3px;
  }
  .lbp-badge {
    position: absolute;
    left: 70px;
    top: 486px;
    width: 174px;
    height: 171px;
    background: var(--badge-bg);
  }
  .contact {
    position: absolute;
    right: 72px;
    top: 553px;
    text-align: right;
    font-style: italic;
    font-size: 28px;
    line-height: 38px;
  }
</style>
</head>
<body>
<main class="card">
  <div class="brand">
    <span class="brand-square"></span>
    <span class="brand-name">MERIDIAN<br>CONSTRUCTION</span>
  </div>

  <header class="person">
    <p class="person-name">Kai Pereira</p>
    <p class="person-role">Director</p>
  </header>

  <h1 class="company-title">MERIDIAN CONSTRUCTION LIMITED</h1>

  <div class="lbp-badge" role="img" aria-label="Licensed building practitioner badge"></div>

  <address class="contact">
    <p>Mobile - 0217364801</p>
    <p>Meridian.Construction@examplemail.test</p>
    <p>48 Halvorsen place,Ashgrove park 2071,Auckland</p>
  </address>
</main>
</body>
</html>
```